New Website for ReBranded Company - CrewBeacon

We have a successful company and website currently but it is a little dated. We have re-branded the company from Harbor Signal Networks to CrewBeacon and have a new logo for the new name. We are looking to build a newer fresher website with the new name. I will need a concept of the home page and one inside page. You can see our current site at https://www.harborsignalnetworks.example and the new site will be https://www.crewbeacon.example .

I also really like the https://www.pathlantern.example/ website. I like ledgerkite.example website. I like the https://skillorbit.example/ website.

See the attached document for layout and some text to use. Use the pictures I attached as opposed to pictures from the old site as much as you can.

Target Market(s)

Business

Industry/Entity Type

Software Service

Number of Pages Required

2 page

Font styles to use
Sans Serif

Requirements
Must have
• Use the colors from my logo. Professional but modern. We want people to feel like our product makes their staff feel safer at work.
Should not have
• Don't use any red or orange (no stop colors).

```html
<!DOCTYPE html>
<html lang="en">
<head>
<meta charset="utf-8">
<title>CrewBeacon — Feel Confident That Your Staff Is Protected</title>
<link rel="stylesheet" href="https://fonts.googleapis.com/css2?family=Montserrat:wght@400;600;700;800&family=Open+Sans:wght@400;600;700&display=swap">
<style>
:root{
  --navy:#15324f;
  --blue:#2b8fd6;
  --blue-soft:#4aa3e0;
  --green:#7cc242;
  --green-dark:#63a832;
  --ink:#1d2530;
  --muted:#5f6b78;
  --line:#d9dee4;
  --grey-bg:#f1f3f5;
  --white:#ffffff;
}
*{box-sizing:border-box;margin:0;padding:0}
html,body{width:1200px;height:4780px;overflow:hidden}
body{font-family:"Open Sans",Arial,sans-serif;color:var(--ink);background:var(--white);position:relative}
h1,h2,h3,h4,.btn,.nav a{font-family:"Montserrat",Arial,sans-serif}
a{text-decoration:none}
.btn{display:inline-block;border-radius:4px;color:var(--white);font-weight:700;font-size:15px;letter-spacing:.5px;padding:16px 30px;text-transform:uppercase;white-space:nowrap}
.btn-green{background:var(--green)}
.btn-blue{background:var(--blue)}
.accent-blue{color:var(--blue)}
.placeholder{position:absolute;border-radius:4px}

/* Hero */
.hero{position:absolute;left:0;top:0;width:1200px;height:720px;overflow:hidden}
.hero-photo{position:absolute;inset:0;background:linear-gradient(100deg,#2a2f33 0%,#5b6166 30%,#c9ced2 55%,#eef0f2 75%,#f6f7f8 100%)}
.nav{position:absolute;left:0;top:0;width:1200px;height:84px;display:flex;align-items:center;padding:0 48px}
.brand{display:flex;align-items:center;gap:10px;font-family:"Montserrat",sans-serif;font-weight:700;font-size:26px;color:var(--white)}
.brand-dot{width:26px;height:26px;border-radius:50%;background:var(--blue)}
.nav-links{margin-left:auto;display:flex;align-items:center;gap:30px}
.nav a{color:var(--ink);font-size:13px;font-weight:700;letter-spacing:.5px}
.nav a.active{background:var(--blue);color:var(--white);padding:10px 14px;border-radius:3px}
.nav a.cta{background:var(--blue);color:var(--white);padding:12px 18px;border-radius:3px}
.hero-copy{position:absolute;left:650px;top:200px;width:520px}
.hero-copy h1{font-size:46px;line-height:1.08;font-weight:800;color:var(--ink);letter-spacing:-.3px}
.hero-copy p{margin-top:16px;font-size:18px;color:var(--green-dark);font-weight:600}
.hero-copy .btn{margin-top:20px;font-size:14px;padding:14px 28px}
.video{position:absolute;left:320px;top:545px;width:560px;height:375px;background:linear-gradient(160deg,#3d4750,#7f8a93 55%,#a8b0b6);border-radius:4px;box-shadow:0 10px 30px rgba(0,0,0,.25)}
.play{position:absolute;left:245px;top:120px}
.video-label{position:absolute;left:0;right:0;top:240px;text-align:center;color:var(--white);font-family:"Montserrat",sans-serif;font-weight:700;font-size:24px}

/* Features */
.features{position:absolute;left:80px;top:1000px;width:1040px;height:310px;border:1px solid var(--line);border-radius:6px;background:var(--white);box-shadow:0 4px 14px rgba(0,0,0,.06);display:flex;padding:24px 30px;gap:30px}
.feature{flex:1}
.feature h3{text-align:center;font-size:20px;font-weight:700;margin-bottom:12px}
.feature-photo{height:150px;border-radius:3px}
.feature-body{display:flex;gap:14px;margin-top:16px;align-items:flex-start}
.feature-body svg{flex:none}
.feature-body p{font-size:16px;line-height:1.4}

/* Alone */
.alone{position:absolute;left:0;top:1380px;width:1200px;height:470px;background:var(--grey-bg)}
.alone-copy{position:absolute;left:80px;top:130px;width:420px}
.alone-copy h2{font-size:27px;font-weight:800;line-height:1.25}
.alone-copy p{margin-top:18px;font-size:16px;line-height:1.55;color:var(--muted)}
.alone-copy .btn{margin-top:22px;font-size:13px;padding:13px 22px}
.alone-screen{left:590px;top:50px;width:540px;height:340px;background:linear-gradient(180deg,#ffffff,#e8edf2);border:1px solid var(--line);box-shadow:0 8px 24px rgba(0,0,0,.12)}
.alone-device{left:490px;top:290px;width:230px;height:120px;background:linear-gradient(135deg,#1e2226,#4a5157);border-radius:30px}

/* Why */
.why{position:absolute;left:0;top:1880px;width:1200px;height:560px;overflow:hidden}
.why h2{position:absolute;left:0;right:0;top:40px;text-align:center;font-size:26px;font-weight:800}
.why-ring{position:absolute;left:0;top:0}
.why-item{position:absolute;text-align:center}
.why-item h4{font-size:18px;font-weight:700;margin-bottom:6px}
.why-item p{font-size:14px;line-height:1.45;color:var(--muted)}
.why-center{position:absolute;left:510px;top:370px;width:180px;height:180px;border-radius:50%;background:#e8f2fb;display:flex;align-items:center;justify-content:center;font-family:"Montserrat",sans-serif;font-weight:700;font-size:20px;color:var(--navy)}

/* Reach */
.reach{position:absolute;left:0;top:2460px;width:1200px;height:585px;background:linear-gradient(180deg,#2a7fc4,#3d94d6 50%,#2c84c9)}
.reach-map{position:absolute;left:80px;top:140px;width:1040px;height:330px;background:radial-gradient(ellipse at center,rgba(255,255,255,.22),rgba(255,255,255,0) 70%)}
.reach-intro{position:absolute;left:0;right:0;top:70px;text-align:center;color:var(--white);font-size:17px}
.reach h2{position:absolute;left:200px;width:800px;top:115px;text-align:center;color:var(--white);font-size:25px;font-weight:800;line-height:1.3}
.stat{position:absolute;color:var(--white)}
.stat .num{font-family:"Montserrat",sans-serif;font-weight:400;font-size:190px;line-height:1}
.stat .cap{font-size:15px;margin-top:6px}
.reach .btn{position:absolute;left:520px;top:470px;font-size:13px;padding:14px 26px}

/* Plan */
.plan{position:absolute;left:0;top:3080px;width:1200px;height:720px}
.plan h2{position:absolute;left:0;right:0;top:50px;text-align:center;font-size:27px;font-weight:800}
.step{position:absolute;top:190px;width:300px;height:340px;border-radius:50%/42%;border:2px solid var(--line);text-align:center;padding:70px 34px 0;background:var(--white)}
.step-icon{position:absolute;left:124px;top:-26px;width:48px;height:48px;border-radius:50%;background:var(--white);border:2px solid var(--green);display:flex;align-items:center;justify-content:center}
.step .tag{font-family:"Montserrat",sans-serif;color:var(--green);font-weight:700;font-size:14px}
.step h3{font-size:20px;font-weight:700;margin:8px 0 12px;line-height:1.25}
.step ul{list-style:none;font-size:14px;line-height:1.7;color:var(--muted)}
.step p{font-size:14px;line-height:1.5;color:var(--muted)}
.plan .btn{position:absolute;left:520px;top:600px;font-size:13px;padding:14px 26px}

/* Connected */
.connected{position:absolute;left:0;top:3820px;width:1200px;height:420px;background:var(--grey-bg)}
.connected-screen{left:240px;top:40px;width:560px;height:340px;background:linear-gradient(180deg,#ffffff,#e6ebf0);border:1px solid var(--line);box-shadow:0 8px 24px rgba(0,0,0,.12)}
.connected-device{left:120px;top:250px;width:260px;height:130px;background:linear-gradient(135deg,#1e2226,#4a5157);border-radius:30px}
.connected-copy{position:absolute;left:760px;top:130px;width:380px}
.connected-copy h2{font-size:26px;font-weight:800;line-height:1.25}
.connected-copy .btn{margin-top:16px;font-size:13px;padding:13px 24px}

/* Newsletter */
.newsletter{position:absolute;left:0;top:4240px;width:1200px;height:100px;display:flex;align-items:center;padding:0 80px}
.newsletter h2{font-size:24px;font-weight:800}
.newsletter-form{margin-left:auto;display:flex}
.newsletter-input{width:340px;height:52px;border:1px solid var(--line);border-radius:3px 0 0 3px;padding:0 18px;font-size:14px;color:#8a949e;display:flex;align-items:center}
.newsletter-form .btn{border-radius:0 3px 3px 0;padding:16px 34px;font-size:14px}

/* Footer */
.footer{position:absolute;left:0;top:4340px;width:1200px;height:440px;background:var(--navy);color:#c5d1dd}
.footer .brand{position:absolute;left:80px;top:50px}
.footer-about{position:absolute;left:80px;top:110px;width:260px;font-size:13px;line-height:1.6}
.socials{position:absolute;left:80px;top:230px;display:flex;gap:12px}
.socials span{width:26px;height:26px;border-radius:50%;background:rgba(255,255,255,.18)}
.footer-col{position:absolute;top:60px}
.footer-col h4{color:var(--white);font-size:14px;font-weight:700;margin-bottom:14px;letter-spacing:.5px}
.footer-col li{list-style:none;font-size:13px;line-height:1.9}
.call{position:absolute;left:900px;top:60px;width:220px;height:70px;border:1px solid rgba(255,255,255,.3);border-radius:4px;display:flex;align-items:center;gap:12px;padding:0 14px}
.call small{display:block;font-size:12px}
.call strong{font-family:"Montserrat",sans-serif;color:var(--white);font-size:17px}
.footer-bottom{position:absolute;left:0;right:0;bottom:0;height:70px;border-top:1px solid rgba(255,255,255,.12);display:flex;justify-content:flex-end;align-items:center;gap:28px;padding:0 80px;font-size:12px}
</style>
</head>
<body>

<section class="hero">
  <div class="hero-photo" role="img" aria-label="Photo of a person in a jacket holding a small panic button device"></div>
  <nav class="nav">
    <div class="brand"><span class="brand-dot"></span>CrewBeacon</div>
    <div class="nav-links">
      <a class="active" href="#">HOME</a>
      <a href="#">BUY BUTTONS</a>
      <a href="#">CUSTOMER LOGIN</a>
      <a class="cta" href="#">EXPLORE YOUR CHOICES</a>
    </div>
  </nav>
  <div class="hero-copy">
    <h1>FEEL CONFIDENT THAT YOUR STAFF IS PROTECTED</h1>
    <p>Get our revolutionary new electronic panic button</p>
    <a class="btn btn-green" href="#">Ready to get started</a>
  </div>
</section>

<div class="video" role="img" aria-label="Video still of a desk phone and workspace">
  <svg class="play" width="70" height="70" viewBox="0 0 70 70"><circle cx="35" cy="35" r="35" fill="#2b8fd6"/><path d="M28 22 L50 35 L28 48 Z" fill="#fff"/></svg>
  <div class="video-label">Watch How It Works</div>
</div>

<section class="features">
  <div class="feature">
    <h3>Problems Stopped</h3>
    <div class="feature-photo" role="img" aria-label="Photo of a covered outdoor walkway" style="background:linear-gradient(180deg,#6a7a86,#3e4a52)"></div>
    <div class="feature-body">
      <svg width="34" height="34" viewBox="0 0 34 34"><circle cx="17" cy="17" r="15" fill="none" stroke="#2b8fd6" stroke-width="2"/><path d="M10 17 L15 22 L24 12" fill="none" stroke="#7cc242" stroke-width="3"/></svg>
      <p>Problems stopped before they start for any type of organization.</p>
    </div>
  </div>
  <div class="feature">
    <h3>Affordable Prices</h3>
    <div class="feature-photo" role="img" aria-label="Photo of panic button devices on a table" style="background:linear-gradient(180deg,#c7ccd0,#8a9298)"></div>
    <div class="feature-body">
      <svg width="34" height="34" viewBox="0 0 34 34"><rect x="6" y="4" width="22" height="26" rx="2" fill="none" stroke="#2b8fd6" stroke-width="2"/><path d="M11 12h12M11 18h12M11 24h7" stroke="#7cc242" stroke-width="2"/></svg>
      <p>Affordable prices starting at $18 per month. No contracts. No hidden costs.</p>
    </div>
  </div>
  <div class="feature">
    <h3>Many Choices</h3>
    <div class="feature-photo" role="img" aria-label="Photo of an office desk phone" style="background:linear-gradient(180deg,#d9dcdf,#6f767c)"></div>
    <div class="feature-body">
      <svg width="34" height="34" viewBox="0 0 34 34"><circle cx="17" cy="17" r="15" fill="none" stroke="#2b8fd6" stroke-width="2"/><path d="M17 9v10" stroke="#7cc242" stroke-width="3"/><circle cx="17" cy="24" r="2" fill="#7cc242"/></svg>
      <p>Alerts by computer, mobile device, text, phone, email, monitoring and E911.</p>
    </div>
  </div>
</section>

<section class="alone">
  <div class="alone-copy">
    <h2>YOUR EMPLOYEES SHOULDN'T FEEL ALONE <span class="accent-blue">WHEN THEY NEED HELP</span></h2>
    <p>Does this problem make you feel frustrated and anxious? Put a simple solution in their hands</p>
    <a class="btn btn-blue" href="#">Ready to get started</a>
  </div>
  <div class="placeholder alone-screen" role="img" aria-label="Laptop screen showing the alert dashboard"></div>
  <div class="placeholder alone-device" role="img" aria-label="Photo of a panic button device on a cord"></div>
</section>

<section class="why">
  <h2>WHY BUSINESSES <span class="accent-blue">CHOOSE US</span></h2>
  <svg class="why-ring" width="1200" height="560" viewBox="0 0 1200 560">
    <circle cx="600" cy="460" r="230" fill="none" stroke="#7cc242" stroke-width="3"/>
    <circle cx="600" cy="230" r="28" fill="#7cc242"/>
    <path d="M588 222h24v14h-14l-6 6v-6h-4z" fill="#fff"/>
    <circle cx="392" cy="362" r="28" fill="#2b8fd6"/>
    <path d="M386 354v18M386 354h10v18" stroke="#fff" stroke-width="3" fill="none"/>
    <circle cx="808" cy="362" r="28" fill="#2b8fd6"/>
    <path d="M808 348l12 5v8c0 8-6 13-12 15-6-2-12-7-12-15v-8z" fill="none" stroke="#fff" stroke-width="2.5"/>
  </svg>
  <div class="why-item" style="left:400px;top:96px;width:400px">
    <h4>Communicate the Way You Want</h4>
    <p>We give you lots of options:<br><strong style="color:var(--ink)">Computer, Mobile, Email, Phone call, Text, E911, Call Center</strong></p>
  </div>
  <div class="why-item" style="left:70px;top:300px;width:290px">
    <h4>Easy to Use</h4>
    <p>Press a button and let the right people know you need help and open a chat window letting everyone talk on resolving their problem</p>
  </div>
  <div class="why-item" style="left:840px;top:300px;width:290px">
    <h4>Cost Effective Protection</h4>
    <p>By leveraging your existing network and equipment we can lower your costs to give better options to your staff</p>
  </div>
  <div class="why-center">CrewBeacon</div>
</section>

<section class="reach">
  <div class="reach-map" role="img" aria-label="World map showing service coverage"></div>
  <p class="reach-intro">We know how scary it can feel to worry about employee safety.</p>
  <h2>THAT'S WHY WE HAVE PROVIDED A WAY FOR CUSTOMERS TO GET HELP TO STAFF EFFECTIVELY IN</h2>
  <div class="stat" style="left:40px;top:240px"><div class="num">45</div><div class="cap" style="padding-left:20px">States in USA</div></div>
  <div class="stat" style="left:990px;top:240px;text-align:right;width:170px"><div class="num">5</div><div class="cap">Countries around the globe</div></div>
  <a class="btn btn-green" href="#">Start my demo</a>
</section>

<section class="plan">
  <h2>SIMPLE <span class="accent-blue">START PLAN</span></h2>
  <svg style="position:absolute;left:0;top:340px" width="1200" height="20"><path d="M400 10H450M750 10H800" stroke="#2b8fd6" stroke-width="2" stroke-dasharray="6 6"/></svg>
  <div class="step" style="left:100px">
    <div class="step-icon"><svg width="22" height="22"><circle cx="11" cy="11" r="7" fill="none" stroke="#2b8fd6" stroke-width="2"/></svg></div>
    <div class="tag">STEP 1</div>
    <h3>Explore Your Choices</h3>
    <ul><li>• Pricing</li><li>• Trial</li><li>• Quotes</li><li>• Hardware</li></ul>
  </div>
  <div class="step" style="left:450px">
    <div class="step-icon"><svg width="22" height="22"><path d="M4 11h14M11 4v14" stroke="#2b8fd6" stroke-width="2"/></svg></div>
    <div class="tag">STEP 2</div>
    <h3>Get Setup</h3>
    <ul><li>• Input Your Alerts</li><li>• Input Your Staff</li><li>• Install Our Software</li></ul>
  </div>
  <div class="step" style="left:800px">
    <div class="step-icon"><svg width="22" height="22"><path d="M4 12l5 5 9-11" fill="none" stroke="#2b8fd6" stroke-width="2"/></svg></div>
    <div class="tag">STEP 3</div>
    <h3>Feel Confident Your Staff is Protected</h3>
    <p>High Five. You just took a major step to getting rid of the anxiety and frustration it's given you.</p>
  </div>
  <a class="btn btn-blue" href="#">Start my demo</a>
</section>

<section class="connected">
  <div class="placeholder connected-screen" role="img" aria-label="Dashboard screen with an emergency chat window"></div>
  <div class="placeholder connected-device" role="img" aria-label="Photo of a panic button on a lanyard"></div>
  <div class="connected-copy">
    <h2><span class="accent-blue">STAY CONNECTED</span> WITH STAFF DURING A CRISIS SITUATION</h2>
    <a class="btn btn-blue" href="#">Start my demo</a>
  </div>
</section>

<section class="newsletter">
  <h2>SUBSCRIBE FOR OUR <span class="accent-blue">NEWSLETTER</span></h2>
  <div class="newsletter-form">
    <div class="newsletter-input">Enter Email Address</div>
    <a class="btn btn-blue" href="#">Subscribe</a>
  </div>
</section>

<footer class="footer">
  <div class="brand"><span class="brand-dot"></span>CrewBeacon</div>
  <p class="footer-about">When employees feel alone during a threatening situation, we give them a way to let the right people know they need help and a space to feel confident that your staff is protected.</p>
  <div class="socials"><span></span><span></span><span></span><span></span></div>
  <div class="footer-col" style="left:400px">
    <h4>SHOP</h4>
    <ul><li>Add Ons</li><li>Start Free Demo</li><li>Get Pricing Quote</li><li>Hardware</li></ul>
  </div>
  <div class="footer-col" style="left:560px">
    <h4>ABOUT</h4>
    <ul><li>Affiliates</li><li>Careers</li><li>Support</li><li>Existing Customers</li><li>Resources</li><li>Blog</li><li>FAQ</li></ul>
  </div>
  <div class="footer-col" style="left:730px">
    <h4>LEGAL</h4>
    <ul><li>Privacy Policy</li><li>Terms of Use</li><li>Data Usage Policy</li></ul>
  </div>
  <div class="call">
    <svg width="30" height="30" viewBox="0 0 24 24"><path d="M6.6 10.8a15 15 0 0 0 6.6 6.6l2.2-2.2a1 1 0 0 1 1-.25 11.4 11.4 0 0 0 3.6.57 1 1 0 0 1 1 1V20a1 1 0 0 1-1 1A17 17 0 0 1 3 4a1 1 0 0 1 1-1h3.5a1 1 0 0 1 1 1c0 1.25.2 2.45.57 3.57a1 1 0 0 1-.25 1z" fill="#7cc242"/></svg>
    <div><small>Call us</small><strong>1-800-555-0142</strong></div>
  </div>
  <div class="footer-bottom">
    <span>PRIVACY POLICY</span><span>TERMS POLICY</span><span>DATA USAGE POLICY</span><span>© 2023 CREWBEACON · ALL RIGHTS RESERVED</span>
  </div>
</footer>

</body>
</html>
```